Summit Builders Web Site / Business Cards

Construction Company that specializes in Water and Fire Damage, Residential ReModels, Landscaping and Building ADU (Accessory Dwelling Unit)

Growing and changing families often need additional space, and a remodeling project can often provide that. Adding a new area, or repurposing an existing one can satisfy this requirement.

Other times, homeowners want to update the look in their kitchen or bathroom with more than just a change of cabinetry or vanity doors and drawers. Whatever your needs are, Summit Builders has skilled workers who are bonded and insured, and ready to make your dreams and visions a reality.

Target Market(s)

Home Owners

Industry/Entity Type

Construction Company

Contact Information for Business Card

Center Logo with our information on the corners

Back side to be Logo Only
Contact Info
CSLB License # 4829516
info@summitbuildersca.example
www.summitbuildersca.example

Coding

Coded - Design and coding required

Number of Pages Required

5+ page

Font styles to use
Serif
Sans Serif

Requirements
Must have
• Using our Logo Colors
Home
About Us
Services
Projects / Portfolio
Contact Us
Nice to have
• Colors matching our Logo
Should not have
• Black because it doesnt match our logo

```html
<!DOCTYPE html>
<html lang="en">
<head>
<meta charset="utf-8">
<title>Summit Builders</title>
<link href="https://fonts.googleapis.com/css2?family=Open+Sans:wght@400;600;700;800&display=swap" rel="stylesheet">
<style>
:root{
  --orange:#f36f21;
  --orange-light:#f7893a;
  --ink:#1e1e1e;
  --body:#333;
  --white:#fff;
  --card-shadow:0 2px 8px rgba(0,0,0,.18);
}
*{margin:0;padding:0;box-sizing:border-box}
html,body{width:1200px;height:5051px;overflow:hidden}
body{font-family:'Open Sans',sans-serif;color:var(--ink);background:var(--white);position:relative}
.abs{position:absolute}
a{color:inherit;text-decoration:none}

/* header */
.topbar{left:318px;top:0;width:882px;height:56px;background:var(--orange);color:#fff;font-size:19px;display:flex;justify-content:flex-end;align-items:center;gap:40px;padding-right:28px}
.topbar span{display:flex;align-items:center;gap:8px}
.brand{left:0;top:0;width:318px;height:176px;display:flex;align-items:center;justify-content:center;gap:10px}
.brand .mark{width:18px;height:18px;background:var(--orange)}
.brand .name{font-size:30px;font-weight:700;color:var(--ink);letter-spacing:1px;line-height:1.05;text-align:left}
.mainnav{left:520px;top:100px;display:flex;gap:24px;font-size:25px;color:var(--ink)}

/* hero */
.hero{left:0;top:176px;width:1200px;height:489px;background:linear-gradient(90deg,#4d5056 0%,#6d7178 45%,#8a8d8a 70%,#6c6d5d 100%)}
.hero-kicker{left:52px;top:300px;color:#fff;font-size:31px}
.hero-title{left:42px;top:352px;background:var(--orange);color:#fff;font-size:50px;font-weight:800;padding:0 14px;line-height:62px;letter-spacing:1px}
.hero-sub{left:55px;top:428px;color:#fff;font-size:30px}
.btn{background:var(--orange);color:#fff;display:flex;align-items:center;justify-content:center}
.hero-btn{left:45px;top:510px;width:170px;height:42px;font-size:23px}

/* about */
.section-mark{width:22px;height:22px;background:var(--orange)}
.about-title{left:55px;top:795px;font-size:52px;font-weight:600;line-height:1}
.about-sub{left:52px;top:855px;font-size:41px;font-weight:700;color:var(--orange)}
.about-lead{left:55px;top:942px;font-size:32px;font-weight:600}
.about-text{left:55px;top:993px;width:555px;font-size:20.5px;line-height:26px;color:var(--body)}
.about-btn{left:55px;top:1163px;width:177px;height:47px;font-size:24px}
.about-photo{left:624px;top:784px;width:543px;height:434px;border-radius:12px;background:linear-gradient(160deg,#8a7a5c,#c9a36c 40%,#6f6a5e 75%,#3f3d3a)}

/* features band */
.features{left:0;top:1250px;width:1200px;height:227px;background:linear-gradient(90deg,var(--orange),var(--orange-light),var(--orange))}
.feature{top:1288px;width:260px;text-align:center;color:#fff;font-size:23px;font-weight:700;line-height:28px}
.feature svg{display:block;margin:0 auto 14px}

/* headings */
.h-center{width:1200px;left:0;text-align:center}
.h-main{font-size:50px;font-weight:600;line-height:1}
.h-sub{font-size:38px;font-weight:700;color:var(--orange);line-height:1}

/* services */
.svc-deco{left:0;top:1780px;width:72px;height:600px;background:linear-gradient(180deg,#e6d9c7,#f2c23a 50%,#d8c4a8)}
.card{background:#fff;box-shadow:var(--card-shadow);border-radius:3px;text-align:center;padding-top:20px}
.card svg{display:block;margin:0 auto 6px}
.card h3{font-size:34px;font-weight:600;line-height:40px}
.card p{font-size:16px;line-height:20px;color:var(--body);margin:16px auto 0;width:260px}
.card .more{display:block;color:var(--orange);font-weight:600;font-size:21px;margin-top:14px}

/* projects */
.projects-bg{left:0;top:2580px;width:1200px;height:705px;background:linear-gradient(90deg,var(--orange),var(--orange-light))}
.proj-title{color:var(--ink)}
.proj-sub{color:#fff}
.proj-main{left:180px;top:2818px;width:842px;height:577px;background:linear-gradient(90deg,#8c8e90 0%,#b9bbbd 50%,#5b5f8f 51%,#3e4678 100%);box-shadow:var(--card-shadow)}
.proj-side-l{left:0;top:2888px;width:78px;height:530px;background:linear-gradient(180deg,#5f7fa8,#8aa0b8)}
.proj-side-r{left:1094px;top:2888px;width:106px;height:530px;background:linear-gradient(180deg,#b09aa0,#8d7b82)}
.proj-caption{left:180px;top:3250px;width:842px;text-align:center;font-size:58px;color:#f5d36b;letter-spacing:2px}
.proj-handle{left:575px;top:3072px;width:70px;height:70px;background:#fff;display:flex;align-items:center;justify-content:center;font-size:22px;color:#555}
.proj-divider{left:608px;top:2818px;width:2px;height:577px;background:#fff}
.arrow{font-size:60px;color:#fff;font-weight:400;top:3070px}
.view-all{left:513px;top:3460px;width:175px;height:45px;font-size:24px}

/* counters */
.counters{left:0;top:3557px;width:1200px;height:236px;background:linear-gradient(90deg,var(--orange),var(--orange-light))}
.counter{top:3598px;width:240px;text-align:center;color:#fff}
.counter b{display:block;font-size:72px;font-weight:600;line-height:80px}
.counter span{font-size:22px;font-weight:700}

/* testimonials */
.avatar{left:157px;top:4053px;width:170px;height:170px;border-radius:50%;background:linear-gradient(160deg,#d9d9d9,#a9a9a9)}
.quote{left:192px;top:4045px;width:833px;height:247px;background:#fff;box-shadow:var(--card-shadow);border-radius:4px}
.quote p{position:absolute;left:178px;top:55px;width:620px;font-size:21px;line-height:26px;color:var(--body)}
.quote .client{position:absolute;left:182px;top:170px;font-size:21px;font-weight:600;color:#444}
.dots{left:594px;top:4328px;display:flex;gap:8px}
.dots i{width:11px;height:11px;border-radius:50%;background:var(--orange);display:block}

/* contact band */
.contact{left:0;top:4398px;width:1200px;height:232px;background:var(--orange);color:#fff}
.contact .col{position:absolute;top:0;height:232px;text-align:center;font-weight:600}
.contact h4{font-size:21px;font-weight:600;margin-top:52px;margin-bottom:22px}
.contact p{font-size:17.5px;line-height:24px}
.contact .rule{position:absolute;top:30px;width:2px;height:172px;background:#fff}

/* footer */
.footer-bg{left:0;top:4630px;width:1200px;height:375px;background:linear-gradient(180deg,#fff,#f4f4f4)}
.footer-brand{left:0;top:4725px;width:1200px;display:flex;justify-content:center;align-items:center;gap:12px}
.footer-brand .mark{width:22px;height:22px;background:var(--orange)}
.footer-brand .name{font-size:40px;font-weight:700;color:var(--ink);letter-spacing:2px}
.social{left:555px;top:4862px;display:flex;gap:18px}
.social i{display:block;width:20px;height:20px;border-radius:50%;background:var(--ink)}
.footnav{left:0;top:4930px;width:1200px;display:flex;justify-content:center;gap:26px;font-size:27px}
.copyright{left:0;top:5005px;width:1200px;height:46px;background:var(--orange);color:#fff;font-size:18px;font-weight:600;display:flex;align-items:center;justify-content:center}
</style>
</head>
<body>

<!-- Header -->
<div class="abs topbar">
  <span><svg width="14" height="20" viewBox="0 0 14 20"><rect x="1" y="1" width="12" height="18" rx="2" fill="none" stroke="#fff" stroke-width="2"/></svg>+1800-555-0142</span>
  <span><svg width="20" height="16" viewBox="0 0 20 16"><rect x="1" y="1" width="18" height="14" fill="none" stroke="#fff" stroke-width="2"/><path d="M1 1l9 8 9-8" fill="none" stroke="#fff" stroke-width="2"/></svg>info@summitbuilders.example</span>
</div>
<div class="abs brand"><div class="mark"></div><div class="name">SUMMIT<br>BUILDERS</div></div>
<nav class="abs mainnav"><a>Home</a><a>About us</a><a>Services</a><a>Projects</a><a>Contact us</a></nav>

<!-- Hero -->
<div class="abs hero" role="img" aria-label="Photo of two engineers in hard hats and safety vests on a construction site with cranes"></div>
<div class="abs hero-kicker">Help you to</div>
<div class="abs hero-title">BUILD YOUR DREAM</div>
<div class="abs hero-sub">WE DELIVER LANDMARK PROJECTS</div>
<a class="abs btn hero-btn">Contact us</a>

<!-- About -->
<div class="abs section-mark" style="left:124px;top:755px"></div>
<div class="abs about-title">ABOUT</div>
<div class="abs about-sub">SUMMIT BUILDERS</div>
<div class="abs about-lead">We deliver landmark projects</div>
<p class="abs about-text">We are rethoric question ran over her cheek When she reached the first hills of the Italic Mountains, she had a last view back on the skyline of her hometown Bookmarksgrove, the headline of Alphabet Village and the subline of her own road, the Line Lane.</p>
<a class="abs btn about-btn">Learn More</a>
<div class="abs about-photo" role="img" aria-label="Photo of three construction workers reviewing plans on a building site at sunset"></div>

<!-- Features -->
<div class="abs features"></div>
<div class="abs feature" style="left:43px">
  <svg width="64" height="76" viewBox="0 0 64 76"><circle cx="32" cy="30" r="24" fill="none" stroke="#fff" stroke-width="3"/><circle cx="32" cy="30" r="15" fill="none" stroke="#fff" stroke-width="2"/><path d="M18 50l-6 22 10-5 6 8 4-20M46 50l6 22-10-5-6 8-4-20" fill="none" stroke="#fff" stroke-width="2.5"/></svg>
  WE'VE REPUTION<br>FOR EXCELLENCE</div>
<div class="abs feature" style="left:347px">
  <svg width="76" height="60" viewBox="0 0 76 60"><path d="M4 20h14l10 10 10-6 10 6 10-10h14M18 20l18 22 6-4 6 4 10-14" fill="none" stroke="#fff" stroke-width="3"/></svg>
  WE BUILD<br>PARTNERSHIPS</div>
<div class="abs feature" style="left:610px">
  <svg width="74" height="74" viewBox="0 0 74 74"><circle cx="37" cy="37" r="33" fill="none" stroke="#fff" stroke-width="3"/><circle cx="37" cy="37" r="25" fill="none" stroke="#fff" stroke-width="2"/><path d="M24 36h8v16h-8zM32 38l8-14c4 0 4 4 3 8h9c2 0 3 3 1 5l-3 12H32" fill="none" stroke="#fff" stroke-width="2.5"/></svg>
  GUIDED BY<br>COMMITMENT</div>
<div class="abs feature" style="left:897px">
  <svg width="76" height="64" viewBox="0 0 76 64"><circle cx="38" cy="14" r="8" fill="none" stroke="#fff" stroke-width="3"/><circle cx="16" cy="24" r="7" fill="none" stroke="#fff" stroke-width="3"/><circle cx="60" cy="24" r="7" fill="none" stroke="#fff" stroke-width="3"/><path d="M24 50c0-14 28-14 28 0M4 58c0-12 22-12 22 0M50 58c0-12 22-12 22 0" fill="none" stroke="#fff" stroke-width="3"/></svg>
  A TEAM OF<br>PROFESSIONALS</div>

<!-- Services -->
<div class="abs section-mark" style="left:589px;top:1535px"></div>
<div class="abs h-center h-main" style="top:1587px">OUR SERVICES</div>
<div class="abs h-center h-sub" style="top:1645px">WHAT WE PROVIDE</div>
<div class="abs svc-deco" role="img" aria-label="Photo of a yellow hard hat and building plans"></div>

<div class="abs card" style="left:68px;top:1745px;width:332px;height:345px">
  <svg width="70" height="70" viewBox="0 0 70 70"><path d="M8 34L35 10l27 24M16 28v34h38V28" fill="none" stroke="#222" stroke-width="3"/><rect x="29" y="42" width="12" height="20" fill="var(--orange)"/></svg>
  <h3>Home<br>Construction</h3>
  <p>Lorem ipsum, or lipsum as it is sometimes known, is dummy text used in laying out print, graphic or web designs</p>
  <a class="more">Read More</a></div>
<div class="abs card" style="left:435px;top:1745px;width:333px;height:345px">
  <svg width="76" height="76" viewBox="0 0 76 76"><rect x="6" y="8" width="64" height="62" fill="none" stroke="#222" stroke-width="3"/><rect x="6" y="8" width="64" height="10" fill="var(--orange)"/><rect x="14" y="26" width="20" height="14" fill="none" stroke="#222" stroke-width="2.5"/><rect x="42" y="26" width="20" height="14" fill="var(--orange)"/><rect x="14" y="48" width="20" height="22" fill="var(--orange)"/><rect x="42" y="48" width="20" height="12" fill="none" stroke="#222" stroke-width="2.5"/></svg>
  <h3>Exterior<br>Design</h3>
  <p>Lorem ipsum, or lipsum as it is sometimes known, is dummy text used in laying out print, graphic or web designs</p>
  <a class="more">Read More</a></div>
<div class="abs card" style="left:790px;top:1745px;width:332px;height:345px">
  <svg width="76" height="82" viewBox="0 0 76 82"><rect x="6" y="4" width="40" height="74" fill="none" stroke="#222" stroke-width="3"/><rect x="46" y="30" width="24" height="48" fill="none" stroke="#222" stroke-width="3"/><g fill="var(--orange)"><rect x="12" y="12" width="8" height="8"/><rect x="26" y="12" width="8" height="8"/><rect x="12" y="26" width="8" height="8"/><rect x="26" y="26" width="8" height="8"/><rect x="12" y="40" width="8" height="8"/><rect x="26" y="40" width="8" height="8"/><rect x="12" y="54" width="8" height="8"/><rect x="26" y="54" width="8" height="8"/></g><g fill="#222"><rect x="52" y="38" width="5" height="5"/><rect x="60" y="38" width="5" height="5"/><rect x="52" y="50" width="5" height="5"/><rect x="60" y="50" width="5" height="5"/></g></svg>
  <h3>Building<br>Remodeling</h3>
  <p>Lorem ipsum, or lipsum as it is sometimes known, is dummy text used in laying out print, graphic or web designs</p>
  <a class="more">Read More</a></div>

<div class="abs card" style="left:68px;top:2138px;width:332px;height:345px">
  <svg width="76" height="82" viewBox="0 0 76 82"><rect x="8" y="6" width="50" height="18" fill="none" stroke="#222" stroke-width="3"/><rect x="14" y="10" width="38" height="10" fill="var(--orange)"/><path d="M58 15h8v22H33v10" fill="none" stroke="#222" stroke-width="3"/><rect x="28" y="47" width="10" height="30" fill="none" stroke="#222" stroke-width="3"/></svg>
  <h3 style="margin-top:14px">Renovations</h3>
  <p>Lorem ipsum, or lipsum as it is sometimes known, is dummy text used in laying out print, graphic or web designs</p>
  <a class="more">Read More</a></div>
<div class="abs card" style="left:428px;top:2138px;width:332px;height:345px">
  <svg width="80" height="70" viewBox="0 0 80 70"><rect x="6" y="8" width="68" height="50" fill="none" stroke="#222" stroke-width="3"/><rect x="14" y="16" width="22" height="14" fill="var(--orange)"/><rect x="42" y="16" width="24" height="6" fill="#222"/><rect x="42" y="26" width="18" height="4" fill="#222"/><rect x="14" y="38" width="16" height="12" fill="none" stroke="#222" stroke-width="2.5"/><rect x="36" y="38" width="30" height="12" fill="var(--orange)"/><path d="M40 58v8M24 66h32" stroke="#222" stroke-width="3"/></svg>
  <h3>Interior<br>Design</h3>
  <p>Lorem ipsum, or lipsum as it is sometimes known, is dummy text used in laying out print, graphic or web designs</p>
  <a class="more">Read More</a></div>
<div class="abs card" style="left:790px;top:2138px;width:332px;height:345px">
  <svg width="76" height="82" viewBox="0 0 76 82"><circle cx="24" cy="24" r="16" fill="none" stroke="#222" stroke-width="3"/><path d="M24 14v10l7 5" fill="none" stroke="#222" stroke-width="3"/><path d="M20 74c0-22 14-32 28-32s28 10 28 32z" fill="var(--orange)"/><rect x="14" y="72" width="60" height="6" fill="#222"/></svg>
  <h3>Safety<br>Management</h3>
  <p>Lorem ipsum, or lipsum as it is sometimes known, is dummy text used in laying out print, graphic or web designs</p>
  <a class="more">Read More</a></div>

<!-- Projects -->
<div class="abs projects-bg"></div>
<div class="abs h-center h-main proj-title" style="top:2656px">OUR PROJECTS</div>
<div class="abs h-center h-sub proj-sub" style="top:2718px">SOME OF RECENT WORK</div>
<div class="abs proj-side-l" role="img" aria-label="Photo of a modern glass commercial building"></div>
<div class="abs proj-side-r" role="img" aria-label="Photo of a suburban house at dusk"></div>
<div class="abs proj-main" role="img" aria-label="Before and after photo of a two-storey house with gray siding, left half black and white, right half in color"></div>
<div class="abs proj-divider"></div>
<div class="abs proj-handle">&lsaquo; &rsaquo;</div>
<div class="abs proj-caption">CONSTRUCTION PROJECT</div>
<div class="abs arrow" style="left:128px">&lsaquo;</div>
<div class="abs arrow" style="left:1035px">&rsaquo;</div>
<a class="abs btn view-all">View All</a>

<!-- Counters -->
<div class="abs counters"></div>
<div class="abs counter" style="left:110px"><b>53</b><span>TOTAL PROJECTS</span></div>
<div class="abs counter" style="left:370px"><b>371</b><span>TOTAL PROJECTS</span></div>
<div class="abs counter" style="left:610px"><b>15</b><span>TOTAL PROJECTS</span></div>
<div class="abs counter" style="left:852px"><b>2600</b><span>TOTAL PROJECTS</span></div>

<!-- Testimonials -->
<div class="abs section-mark" style="left:610px;top:3865px"></div>
<div class="abs h-center h-main" style="top:3905px;left:20px">TESTIMONIALS</div>
<div class="abs h-center h-sub" style="top:3965px;left:20px;font-size:37px">WHAT OUR CLIENTS SAY</div>
<div class="abs quote">
  <p>Lorem ipsum, or lipsum as it is sometimes known, is dummy text used in laying out print, graphic<br>or web designs</p>
  <div class="client">Client Name</div>
</div>
<div class="abs avatar" role="img" aria-label="Client portrait photo"></div>
<div class="abs dots"><i></i><i></i><i></i></div>

<!-- Contact band -->
<div class="abs contact">
  <div class="col" style="left:0;width:417px">
    <h4>&#9719; WORKING HOURS</h4>
    <p>Monday – Friday: 10:00 – 16:00<br>Saturday: 12:00 – 15:00<br>Sunday and Holidays: 09:00 – 12:00</p>
  </div>
  <div class="rule" style="left:416px"></div>
  <div class="col" style="left:417px;width:348px">
    <h4 style="margin-top:58px">ADDRESS</h4>
    <p>410 Ridgeview Ave<br>Fairhaven, CA 90000</p>
  </div>
  <div class="rule" style="left:764px"></div>
  <div class="col" style="left:766px;width:434px">
    <h4>CONTACT</h4>
    <p>Daniel R Hale | Branch Manager<br>Office : 555-010-4410<br>Direct : 555-010-2096 &nbsp; Fax : 555-010-7210<br>dhale@summitbuilders.example</p>
  </div>
</div>

<!-- Footer -->
<div class="abs footer-bg" role="img" aria-label="Faint line drawing of a city skyline"></div>
<div class="abs footer-brand"><div class="mark"></div><div class="name">SUMMIT BUILDERS</div></div>
<div class="abs social"><i></i><i></i><i></i></div>
<nav class="abs footnav"><a>Home</a><a>About us</a><a>Services</a><a>Projects</a><a>Contact us</a></nav>
<div class="abs copyright">Copyright © 2020 Summit Builders</div>

</body>
</html>
```